Business Cards for Law Office of Miriam T. Haskell

I need a business card for my new estate planning law firm. I have attached my logo. I would like a design that is professional but not too formal or stuffy.

Target Market(s)

Professionals (lawyers, doctors, businesswomen) between the age of 30 and 50 who are tech-savvy and educated.

Industry/Entity Type

Lawyer

Contact Information for Business Card

Miriam T. Haskell

582 E. 67th Street
9th Floor
New York, NY 10065

Phone: (855) 407-6218
Direct: (917) 563-0472
Email: Miriam@MiriamTHaskellLaw.example
www.MiriamTHaskellLaw.example

Font styles to use
Other font styles liked:
• Corbel

Requirements
Must have
• On the front:
• Miriam T. Haskell, Esq.
• Owner & Founder
• 582 E. 67th Street
• 9th Floor
• New York, NY 10065
• Phone: (855) 407-6218
• Direct: (917) 563-0472
• Email: miriam@miriamthaskelllaw.example
• www.miriamthaskelllaw.example
• On the back:
• LOGO
Nice to have
• I want it to be professional but not too formal or stuffy. Please choose colors that go with my logo.
Should not have
• I don't want TOO MUCH color. Some color is good, but not too much.

```html
<!DOCTYPE html>
<html lang="en">
<head>
<meta charset="utf-8">
<title>Business Cards – Law Office of Miriam T. Haskell</title>
<link href="https://fonts.googleapis.com/css2?family=Open+Sans:wght@400;600&display=swap" rel="stylesheet">
<style>
  :root {
    --page-bg: #ecebe8;
    --card-bg: #1f2a34;
    --ink-light: #f1f1f1;
    --accent-orange: #f08a1c;
    --brand-purple: #a05bc4;
    --rule-rose: #d9958c;
  }
  * { margin: 0; padding: 0; box-sizing: border-box; }
  html, body {
    width: 1200px; height: 900px; overflow: hidden;
    background: var(--page-bg);
    font-family: "Open Sans", Arial, sans-serif;
  }
  .card {
    position: absolute;
    width: 555px; height: 343px;
    background: var(--card-bg);
    box-shadow: 0 8px 24px rgba(0,0,0,0.25);
    color: var(--ink-light);
  }
  .card--front { left: 238px; top: 62px; }
  .card--back  { left: 459px; top: 519px; }

  .brand {
    position: absolute;
    display: flex; align-items: center; gap: 12px;
  }
  .brand__mark {
    width: 14px; height: 14px;
    background: var(--brand-purple);
  }
  .brand__name {
    font-weight: 600;
    color: var(--brand-purple);
    letter-spacing: 0.5px;
    white-space: nowrap;
  }
  .card--front .brand { left: 40px; top: 62px; }
  .card--front .brand__name { font-size: 26px; }
  .card--back .brand { left: 86px; top: 155px; }
  .card--back .brand__name { font-size: 28px; }

  .holder {
    position: absolute; right: 22px; top: 172px;
    text-align: right;
  }
  .holder__name { color: var(--accent-orange); font-weight: 600; font-size: 17px; line-height: 22px; }
  .holder__title { font-size: 14px; line-height: 18px; }

  .address {
    position: absolute; left: 36px; top: 248px;
    font-size: 14.5px; line-height: 20px;
  }
  .address__label { color: var(--accent-orange); font-weight: 600; }
  .address__direct { margin-bottom: 8px; }

  .contact {
    position: absolute; right: 22px; top: 250px;
    list-style: none; text-align: right;
    font-size: 14.5px; line-height: 20.5px;
  }
  .contact li { display: flex; justify-content: flex-end; align-items: center; gap: 9px; }
  .contact svg { width: 11px; height: 11px; fill: var(--accent-orange); flex: none; }
</style>
</head>
<body>

<section class="card card--front" aria-label="Business card front">
  <div class="brand">
    <span class="brand__mark"></span>
    <span class="brand__name">Law Office of Miriam T. Haskell</span>
  </div>

  <div class="holder">
    <p class="holder__name">Miriam T. Haskell, Esq.</p>
    <p class="holder__title">Owner &amp; Founder</p>
  </div>

  <div class="address">
    <p class="address__direct"><span class="address__label">Direct:</span> (917) 563-0472</p>
    <p>582 E. 67th Street 9th Floor</p>
    <p>New York, NY 10065</p>
  </div>

  <ul class="contact">
    <li>(855) 407-6218
      <svg viewBox="0 0 24 24" aria-hidden="true"><path d="M6.6 10.8a15.1 15.1 0 0 0 6.6 6.6l2.2-2.2a1 1 0 0 1 1-.25 11.4 11.4 0 0 0 3.6.57 1 1 0 0 1 1 1V20a1 1 0 0 1-1 1A17 17 0 0 1 3 4a1 1 0 0 1 1-1h3.5a1 1 0 0 1 1 1c0 1.25.2 2.45.57 3.57a1 1 0 0 1-.25 1z"/></svg>
    </li>
    <li>miriam@miriamthaskelllaw.example
      <svg viewBox="0 0 24 24" aria-hidden="true"><path d="M2 5h20v14H2z M4 7v.5l8 5 8-5V7l-8 5z" fill-rule="evenodd"/></svg>
    </li>
    <li>www.miriamthaskelllaw.example
      <svg viewBox="0 0 24 24" aria-hidden="true"><circle cx="12" cy="12" r="10"/></svg>
    </li>
  </ul>
</section>

<section class="card card--back" aria-label="Business card back">
  <div class="brand">
    <span class="brand__mark"></span>
    <span class="brand__name">Law Office of Miriam T. Haskell</span>
  </div>
</section>

</body>
</html>
```